Infographic for Anesthesia Management Company

I would like my Anesthesia Management company, Veltrin Anesthesia, service information placed into a infographic for use on a brochure and webpage. Please focus on just the infographic.
-Veltrin Services text to be placed into infographic attached in word file.
-Two Vector infographic templates attached as well. I am open to either option, or alternative layout suggestion.
-Please match color scheme to veltrinanesthesia-example.com
-Veltrin logo attached.
Thank you for your help!
Marvin
Target Market(s)
Surgery Centers
Industry/Entity Type
It Company
Font styles to use
Requirements
Must have
- Professional Look.
- Easy to read text.
- Cohesive branding
Nice to have
- Please see attached Vector examples.

```html
<!DOCTYPE html>
<html lang="en">
<head>
<meta charset="utf-8">
<title>Veltrin Anesthesia – Provider Recruitment Infographic</title>
<link href="https://fonts.googleapis.com/css2?family=Hind:wght@500;600;700&family=Arimo:wght@400;700&display=swap" rel="stylesheet">
<style>
:root{
  --page:#f2eee8;
  --purple:#846f97;
  --purple-text:#7e6798;
  --mustard:#c6a52d;
  --lime:#b8d44f;
  --teal:#15b89f;
  --white:#ffffff;
  --ink:#1f1f1f;
  --body:#3b3b3b;
  --soft:#e7e7e7;
}
*{box-sizing:border-box;margin:0;padding:0}
html,body{width:1030px;height:1200px;overflow:hidden}
body{background:var(--page);font-family:"Arimo",Arial,sans-serif;position:relative}
.sheet{position:absolute;left:66px;width:894px;height:544px;background:var(--white);box-shadow:0 3px 10px rgba(0,0,0,.18)}
.sheet--colour{top:33px}
.sheet--clean{top:606px}
.sheet__header{height:111px;display:flex;align-items:center;justify-content:center;text-align:center;color:var(--white);font-family:"Hind",sans-serif;font-weight:700;font-size:30px;line-height:38px;letter-spacing:.3px}
.sheet--colour .sheet__header{background:var(--purple)}
.sheet--clean .sheet__header{background:var(--teal);height:90px;padding-top:2px;position:relative}
.sheet--clean .sheet__header::after{content:"";position:absolute;left:120px;width:642px;top:88px;height:18px;background:var(--teal);border-radius:0 0 14px 14px}
.sheet--clean .sheet__header span{position:relative;z-index:1;top:8px}

.panel{position:absolute;top:117px;height:222px;font-size:9.6px;line-height:12px}
.panel--one{left:23px;width:292px}
.panel--two{left:324px;width:292px}
.panel--three{left:623px;width:246px}
.sheet--clean .panel{top:118px;background:var(--white);box-shadow:0 1px 5px rgba(0,0,0,.14)}
.sheet--clean .panel--one{width:294px}
.sheet--clean .panel--two{left:327px;width:294px}
.sheet--clean .panel--three{left:629px;width:248px}
.sheet--colour .panel{color:var(--white)}
.sheet--colour .panel--one{background:var(--mustard)}
.sheet--colour .panel--two{background:var(--purple)}
.sheet--colour .panel--three{background:var(--lime)}
.panel--one::after,.panel--two::after{content:"";position:absolute;right:-16px;top:96px;border-top:16px solid transparent;border-bottom:16px solid transparent;border-left:16px solid;z-index:2}
.sheet--colour .panel--one::after{border-left-color:var(--mustard)}
.sheet--colour .panel--two::after{border-left-color:var(--purple)}
.sheet--clean .panel--one::after,.sheet--clean .panel--two::after{border-left-color:var(--soft);right:-14px}

.panel__icon{position:absolute}
.panel__title{position:absolute;font-family:"Hind",sans-serif;font-weight:700;font-size:21px;line-height:22px;letter-spacing:.2px}
.panel__sub{position:absolute;font-family:"Hind",sans-serif;font-weight:600;font-size:14.5px;line-height:18px}
.sheet--clean .panel__title{color:var(--ink)}
.sheet--clean .panel__sub{color:var(--purple-text)}
.sheet--colour .panel__title{color:var(--ink)}
.sheet--colour .panel__sub{color:var(--white)}
.rule{position:absolute;border-top:1.5px dotted currentColor;opacity:.85}
.sheet--clean .rule{color:#555}

.ticks{position:absolute;list-style:none}
.ticks li{position:relative;padding-left:24px;margin-bottom:10px}
.ticks svg{position:absolute;left:0;top:2px;width:14px;height:14px}
.sheet--clean .ticks{color:var(--body)}
.sheet--clean .ticks svg{color:var(--teal)}
.sheet--colour .ticks svg{color:var(--white)}

.placeholder-icon{border-radius:10px}

.care{position:absolute;left:23px;top:345px;width:846px;height:183px;border-radius:0 0 14px 14px;font-size:9.6px;line-height:12px}
.sheet--colour .care{background:var(--white);box-shadow:0 1px 5px rgba(0,0,0,.12)}
.sheet--colour .care__main{position:absolute;left:0;top:0;width:581px;height:183px;background:var(--teal);border-radius:0 0 0 14px;color:var(--white)}
.sheet--clean .care{background:var(--white);box-shadow:0 1px 5px rgba(0,0,0,.14);top:346px}
.sheet--clean .care__main{position:absolute;left:0;top:0;width:585px;height:183px;color:var(--body)}
.care__title{position:absolute;left:102px;top:30px;font-family:"Hind",sans-serif;font-weight:700;font-size:22px;line-height:26px;color:var(--ink)}
.care__sub{position:absolute;left:102px;top:84px;font-family:"Hind",sans-serif;font-weight:600;font-size:14.5px;line-height:18px}
.sheet--colour .care__sub{color:var(--white)}
.sheet--clean .care__sub{color:var(--purple-text)}
.care .ticks{left:268px;top:33px;width:300px}
.care .ticks li{margin-bottom:11px}

.contact{position:absolute;right:0;top:0;width:265px;height:183px;text-align:center}
.sheet--clean .contact{border-left:1.5px solid #9b8aad;top:22px;height:146px;width:262px}
.sheet--clean .contact__inner{margin-top:-22px}
.brand{margin-top:32px;font-family:"Hind",sans-serif;font-weight:700;font-size:26px;line-height:30px;color:var(--teal)}
.phone{margin-top:18px;font-family:"Hind",sans-serif;font-weight:600;font-size:32px;line-height:34px;color:var(--purple-text)}
.web{margin-top:4px;font-family:"Hind",sans-serif;font-weight:600;font-size:14px;color:var(--ink)}
.mail{font-family:"Hind",sans-serif;font-weight:600;font-size:10.5px;color:var(--ink)}
</style>
</head>
<body>

<svg width="0" height="0" style="position:absolute" aria-hidden="true">
  <symbol id="tick" viewBox="0 0 14 14"><circle cx="7" cy="7" r="6" fill="none" stroke="currentColor" stroke-width="1.5"/><path d="M4.2 7.2l2 2 3.8-4" fill="none" stroke="currentColor" stroke-width="1.6" stroke-linecap="round" stroke-linejoin="round"/></symbol>
  <symbol id="target" viewBox="0 0 60 60"><circle cx="26" cy="34" r="23" fill="none" stroke="currentColor" stroke-width="5"/><circle cx="26" cy="34" r="14" fill="none" stroke="currentColor" stroke-width="5"/><circle cx="26" cy="34" r="5" fill="currentColor"/><path d="M26 34L52 8" stroke="currentColor" stroke-width="3.5" stroke-linecap="round"/><path d="M47 4l9-3-3 9-8 2z" fill="currentColor"/></symbol>
  <symbol id="clipboard" viewBox="0 0 50 66"><rect x="3" y="8" width="38" height="52" rx="4" fill="none" stroke="currentColor" stroke-width="3.5"/><rect x="13" y="3" width="18" height="9" rx="2" fill="currentColor"/><path d="M9 22l3 3 5-5M9 34l3 3 5-5M9 46l3 3 5-5" fill="none" stroke="currentColor" stroke-width="2.5"/><path d="M21 24h14M21 36h14M21 48h8" stroke="currentColor" stroke-width="2.5"/><circle cx="37" cy="52" r="11" fill="currentColor"/><path d="M32 52l4 4 7-8" fill="none" stroke="#fff" stroke-width="3"/></symbol>
</svg>

<!-- Colour version -->
<section class="sheet sheet--colour">
  <header class="sheet__header"><span>ANESTHESIA PROVIDER RECRUITMENT,<br>CREDENTIALING, AND STAFFING</span></header>

  <article class="panel panel--one">
    <div class="panel__icon placeholder-icon" role="img" aria-label="Handshake icon" style="left:12px;top:24px;width:66px;height:42px;background:rgba(255,255,255,.85)"></div>
    <h2 class="panel__title" style="left:80px;top:26px">PROFESSIONALISM</h2>
    <p class="panel__sub" style="left:80px;top:50px">ASC Stakeholder Satisfaction</p>
    <div class="rule" style="left:48px;top:74px;width:228px"></div>
    <ul class="ticks" style="left:52px;top:84px;width:212px">
      <li><svg><use href="#tick"/></svg>Share our personal network of highly qualified anesthesia providers</li>
      <li><svg><use href="#tick"/></svg>Create continuity between anesthesia, surgeon, and ASC staff</li>
      <li><svg><use href="#tick"/></svg>Guarantee every anesthesia provider upholds clinical excellence</li>
      <li><svg><use href="#tick"/></svg>Coordinate staffing to meet your scheduled case volume</li>
    </ul>
  </article>

  <article class="panel panel--two">
    <svg class="panel__icon" style="left:20px;top:12px;width:50px;height:66px;color:var(--white)"><use href="#clipboard"/></svg>
    <h2 class="panel__title" style="left:88px;top:26px">ACCOUNTABILITY</h2>
    <p class="panel__sub" style="left:88px;top:50px">Meeting Accreditation<br>Requirements</p>
    <div class="rule" style="left:40px;top:93px;width:212px"></div>
    <ul class="ticks" style="left:40px;top:102px;width:222px">
      <li><svg><use href="#tick"/></svg>Partner with your surgery center to ensure anesthesia policies and procedures are up to current ASC credentialing standards</li>
    </ul>
    <p class="panel__sub" style="left:66px;top:147px">In-House Billing</p>
    <div class="rule" style="left:34px;top:170px;width:212px"></div>
    <ul class="ticks" style="left:40px;top:176px;width:222px">
      <li><svg><use href="#tick"/></svg>Dedicated in-house billers ensure anesthesia billing is processed correctly the first time</li>
    </ul>
  </article>

  <article class="panel panel--three">
    <svg class="panel__icon" style="left:10px;top:14px;width:60px;height:60px;color:var(--white)"><use href="#target"/></svg>
    <h2 class="panel__title" style="left:77px;top:38px">EFFICIENCY</h2>
    <p class="panel__sub" style="left:74px;top:60px">Thought Leadership</p>
    <div class="rule" style="left:40px;top:87px;width:170px"></div>
    <ul class="ticks" style="left:56px;top:97px;width:170px">
      <li><svg><use href="#tick"/></svg>Stipend free anesthesia services</li>
      <li><svg><use href="#tick"/></svg>Proprietary and data-driven process to maintain on-time surgery flow</li>
    </ul>
  </article>

  <article class="care">
    <div class="care__main">
      <div class="placeholder-icon" role="img" aria-label="Heart held in hands icon" style="position:absolute;left:18px;top:23px;width:66px;height:66px;background:rgba(255,255,255,.85)"></div>
      <h2 class="care__title">PATIENT<br>SAFETY</h2>
      <p class="care__sub">Clinical Guidance and<br>Quality Improvement</p>
      <ul class="ticks">
        <li><svg><use href="#tick"/></svg>Pre-operative protocols to minimize cancellations<br>and optimize patient outcomes</li>
        <li><svg><use href="#tick"/></svg>Patient selection criteria to ensure suitable<br>surgical candidates</li>
        <li><svg><use href="#tick"/></svg>Education programs to engage the clinical<br>staff</li>
        <li><svg><use href="#tick"/></svg>Evidence based multimodal pain management protocol to facilitate a timely discharge and reduce patient side effects</li>
      </ul>
    </div>
    <div class="contact">
      <p class="brand">Veltrin Anesthesia</p>
      <p class="phone">(555) 014-2290</p>
      <p class="web">www.veltrinanesthesia-example.com</p>
      <p class="mail">marvinb@veltrinanesthesia-example.com</p>
    </div>
  </article>
</section>

<!-- Clean version -->
<section class="sheet sheet--clean">
  <header class="sheet__header"><span>ANESTHESIA PROVIDER RECRUITMENT,<br>CREDENTIALING, AND STAFFING</span></header>

  <article class="panel panel--one">
    <div class="panel__icon placeholder-icon" role="img" aria-label="Handshake icon" style="left:12px;top:22px;width:66px;height:42px;background:var(--teal)"></div>
    <h2 class="panel__title" style="left:80px;top:26px">PROFESSIONALISM</h2>
    <p class="panel__sub" style="left:80px;top:50px">ASC Stakeholder Satisfaction</p>
    <div class="rule" style="left:48px;top:74px;width:232px"></div>
    <ul class="ticks" style="left:52px;top:84px;width:212px">
      <li><svg><use href="#tick"/></svg>Share our personal network of highly qualified anesthesia providers</li>
      <li><svg><use href="#tick"/></svg>Create continuity between anesthesia, surgeon, and ASC staff</li>
      <li><svg><use href="#tick"/></svg>Guarantee every anesthesia provider upholds clinical excellence</li>
      <li><svg><use href="#tick"/></svg>Coordinate staffing to meet your scheduled case volume</li>
    </ul>
  </article>

  <article class="panel panel--two">
    <svg class="panel__icon" style="left:20px;top:12px;width:50px;height:66px;color:var(--teal)"><use href="#clipboard"/></svg>
    <h2 class="panel__title" style="left:88px;top:26px">ACCOUNTABILITY</h2>
    <p class="panel__sub" style="left:88px;top:50px">Meeting Accreditation<br>Requirements</p>
    <div class="rule" style="left:40px;top:93px;width:214px"></div>
    <ul class="ticks" style="left:40px;top:102px;width:222px">
      <li><svg><use href="#tick"/></svg>Partner with your surgery center to ensure anesthesia policies and procedures are up to current ASC credentialing standards</li>
    </ul>
    <p class="panel__sub" style="left:66px;top:147px">In-House Billing</p>
    <div class="rule" style="left:34px;top:170px;width:214px"></div>
    <ul class="ticks" style="left:40px;top:176px;width:222px">
      <li><svg><use href="#tick"/></svg>Dedicated in-house billers ensure anesthesia billing is processed correctly the first time</li>
    </ul>
  </article>

  <article class="panel panel--three">
    <svg class="panel__icon" style="left:10px;top:12px;width:60px;height:60px;color:var(--teal)"><use href="#target"/></svg>
    <h2 class="panel__title" style="left:78px;top:36px">EFFICIENCY</h2>
    <p class="panel__sub" style="left:75px;top:58px">Thought Leadership</p>
    <div class="rule" style="left:40px;top:87px;width:170px"></div>
    <ul class="ticks" style="left:56px;top:98px;width:170px">
      <li><svg><use href="#tick"/></svg>Stipend free anesthesia services</li>
      <li><svg><use href="#tick"/></svg>Proprietary and data-driven process to maintain on-time surgery flow</li>
    </ul>
  </article>

  <article class="care">
    <div class="care__main">
      <div class="placeholder-icon" role="img" aria-label="Heart held in hands icon" style="position:absolute;left:18px;top:23px;width:66px;height:66px;background:var(--teal)"></div>
      <h2 class="care__title">PATIENT<br>SAFETY</h2>
      <p class="care__sub">Clinical Guidance and<br>Quality Improvement</p>
      <ul class="ticks">
        <li><svg><use href="#tick"/></svg>Pre-operative protocols to minimize cancellations<br>and optimize patient outcomes</li>
        <li><svg><use href="#tick"/></svg>Patient selection criteria to ensure suitable<br>surgical candidates</li>
        <li><svg><use href="#tick"/></svg>Education programs to engage the clinical<br>staff</li>
        <li><svg><use href="#tick"/></svg>Evidence based multimodal pain management protocol to facilitate a timely discharge and reduce patient side effects</li>
      </ul>
    </div>
    <div class="contact">
      <div class="contact__inner">
        <p class="brand">Veltrin Anesthesia</p>
        <p class="phone">(555) 014-2290</p>
        <p class="web">www.veltrinanesthesia-example.com</p>
        <p class="mail">marvinb@veltrinanesthesia-example.com</p>
      </div>
    </div>
  </article>
</section>

</body>
</html>
```